Lanternfield Advisory logo/business card design -- a digital consulting company

I've just restarted a consulting company I had years ago--Lanternfield Advisory. Now I need a new business card and updated logo. The original logo was simple enough: a chart-like progression atop a grid (see the attached file). I do strategy work, and the chart is meant to show incremental growth and profit. I'd like the reincarnation of my logo to be 3D, with both the grid and arrow rotated on their axis.

I'll want to use the logo on my website as well. I'm open to color schemes, fonts, etc.

Target Market(s)

Business-to-Business. Target market is corporate.

Industry/Entity Type

Business

Contact Information for Business Card

Logo on one-side; name and other contact info on the back

Font styles to use
Serif
Sans Serif

Requirements
Nice to have
• Lanternfield Advisory refers to the concept of "bootstrapping" or making incremental changes to grow with minimal risk and financial exposure, and self-sufficiency (think of the phrase "to pull oneself by one's bootstraps.")

```html
<!DOCTYPE html>
<html lang="en">
<head>
<meta charset="utf-8">
<title>Lanternfield Advisory – Identity and Business Card</title>
<link href="https://fonts.googleapis.com/css2?family=Michroma&family=Montserrat:wght@400;600&display=swap" rel="stylesheet">
<style>
  :root {
    --stage: #3b322d;
    --sheet: #ffffff;
    --card-dark: #0d0d0e;
    --card-light: #ffffff;
    --brand-grey: #555555;
    --brand-violet: #4b3f9e;
    --ink: #161616;
    --on-dark: #e8e8ec;
  }
  * { box-sizing: border-box; margin: 0; padding: 0; }
  html, body { width: 1200px; height: 945px; overflow: hidden; }
  body { background: var(--sheet); font-family: "Montserrat", sans-serif; }

  .canvas { position: relative; width: 1200px; height: 945px; }

  .card-stage {
    position: absolute; left: 0; top: 0; width: 1200px; height: 670px;
    background: var(--stage);
  }
  .card {
    position: absolute; top: 215px; width: 420px; height: 240px;
    border-radius: 14px;
  }
  .card--front { left: 150px; background: var(--card-dark); display: flex; align-items: center; justify-content: center; }
  .card--back { left: 630px; background: var(--card-light); }

  .wordmark {
    display: flex; align-items: center; gap: 12px;
    font-family: "Michroma", sans-serif; letter-spacing: 0.08em;
    text-transform: uppercase; white-space: nowrap;
  }
  .wordmark__square { width: 16px; height: 16px; background: var(--brand-violet); flex: none; }
  .card--front .wordmark { font-size: 17px; color: var(--on-dark); }

  .card--back .wordmark { position: absolute; left: 30px; top: 52px; font-size: 11px; color: var(--brand-grey); gap: 8px; }
  .card--back .wordmark__square { width: 10px; height: 10px; }

  .contact { position: absolute; left: 232px; top: 112px; color: var(--ink); }
  .contact__name { font-size: 17px; font-weight: 600; }
  .contact__role { font-size: 11px; color: var(--brand-violet); margin-bottom: 10px; }
  .contact__line { display: flex; align-items: center; gap: 8px; font-size: 10.5px; margin-top: 5px; }
  .contact__line svg { width: 11px; height: 11px; fill: var(--brand-violet); flex: none; }

  .logo-lockup {
    position: absolute; left: 0; top: 670px; width: 1200px; height: 275px;
    display: flex; align-items: center; justify-content: center;
  }
  .logo-lockup .wordmark { font-size: 38px; color: var(--brand-grey); gap: 24px; }
  .logo-lockup .wordmark__square { width: 34px; height: 34px; }
</style>
</head>
<body>
<main class="canvas">
  <section class="card-stage">
    <article class="card card--front">
      <div class="wordmark"><span class="wordmark__square"></span><span>Lanternfield Advisory</span></div>
    </article>

    <article class="card card--back">
      <div class="wordmark"><span class="wordmark__square"></span><span>Lanternfield Advisory</span></div>
      <div class="contact">
        <p class="contact__name">Your Name</p>
        <p class="contact__role">Job Title</p>
        <p class="contact__line">
          <svg viewBox="0 0 12 12" aria-hidden="true"><path d="M1 4c0-2 2-3 5-3s5 1 5 3v1H8V4H4v1H1zM3 6h6l2 5H1z"/></svg>
          000 000 0000
        </p>
        <p class="contact__line">
          <svg viewBox="0 0 12 12" aria-hidden="true"><path d="M0 2h12v1L6 7 0 3zM0 4.5l6 4 6-4V10H0z"/></svg>
          youremail@lanternfield.com
        </p>
        <p class="contact__line">
          <svg viewBox="0 0 12 12" aria-hidden="true"><path d="M6 0a6 6 0 1 0 0 12A6 6 0 0 0 6 0zm0 1c.8 0 1.6 1.8 1.8 4.5H4.2C4.4 2.8 5.2 1 6 1zM1 6.5h2.2c.1 1.6.4 3 .9 3.9A5 5 0 0 1 1 6.5zm0-1a5 5 0 0 1 3.1-3.9c-.5.9-.8 2.3-.9 3.9zm5 5.5c-.8 0-1.6-1.8-1.8-4.5h3.6C7.6 9.2 6.8 11 6 11zm1.9-.6c.5-.9.8-2.3.9-3.9H11a5 5 0 0 1-3.1 3.9zm.9-4.9c-.1-1.6-.4-3-.9-3.9A5 5 0 0 1 11 5.5z"/></svg>
          www.lanternfield.com
        </p>
      </div>
    </article>
  </section>

  <section class="logo-lockup">
    <div class="wordmark"><span class="wordmark__square"></span><span>Lanternfield Advisory</span></div>
  </section>
</main>
</body>
</html>
```